Vitamin B12 Liquid Drops Label

hi, i need a label designed for my vitamin b12 drops that i am going to be selling on bazaarly. the label needs to quickly capture the attention of a buyer as he or she is scrolling through the thumbnail search results on bazaarly.net my brand is called zulmo. i already have an example brand logo i will be using, however, i need help designing the rest of the label. attached are some examples of labels i like for other supplements.some of these examples are pink. i do not want pink. please go for a blue/green color scheme. THE DESIGN MUST BE BOLD

Target Market(s)

adults ages 30 - 64

Font styles to use
Sans Serif

Colors
0455a3
cedeed
3176b5
85acd3
cfdeed
9bcb3b
abd037
cadf82
00a990

Requirements
Must have
• - bold design
• - somewhat gender-neutral color scheme because this will be used equally by men and women
• - B12 MUST be very prominent and visible on the label
Should not have
• - it should not be "crunchy" looking

```html
<!DOCTYPE html>
<html lang="en">
<head>
<meta charset="utf-8">
<title>Zulmo Vitamin B12 – Liquid Drops Label</title>
<link rel="stylesheet" href="https://fonts.googleapis.com/css2?family=Source+Sans+3:wght@300;400;700;900&display=swap">
<style>
  :root {
    --page-bg: #f1f1f1;
    --label-deep: #3a9fdc;
    --label-mid: #7cc6ee;
    --label-light: #c9ecfb;
    --brand-blue: #1f5ccc;
    --band-blue: #0c4fb8;
    --accent-blue: #2a6fd6;
    --silver-light: #f4f6f8;
    --silver-dark: #9aa3ad;
    --visual-core: #2f8fd6;
    --white: #ffffff;
  }
  * { margin: 0; padding: 0; box-sizing: border-box; }
  html, body {
    width: 1200px; height: 900px; overflow: hidden;
    background: var(--page-bg);
    font-family: "Source Sans 3", Arial, sans-serif;
  }
  .label {
    position: absolute; left: 280px; top: 50px;
    width: 640px; height: 800px; overflow: hidden;
    background:
      radial-gradient(circle at 65% 26%, var(--label-light) 0%, var(--label-mid) 40%, transparent 72%),
      linear-gradient(90deg, var(--label-deep) 0%, var(--label-mid) 45%, var(--label-light) 100%);
  }
  .brand-name {
    position: absolute; left: 62px; top: 80px;
    width: 160px; height: 620px;
    display: flex; align-items: center; justify-content: center;
    writing-mode: vertical-rl; transform: rotate(180deg);
    font-weight: 900; font-size: 180px; line-height: 1; letter-spacing: 4px;
    color: var(--brand-blue); white-space: nowrap;
  }
  .drop-visual {
    position: absolute; left: 250px; top: 45px; width: 300px; height: 330px;
    border-radius: 8px;
    background: radial-gradient(ellipse at 50% 50%, var(--visual-core) 0%, rgba(124,198,238,0.55) 40%, rgba(201,236,251,0) 70%);
  }
  .product-title { color: var(--white); font-weight: 400; }
  .vitamin {
    position: absolute; left: 262px; top: 394px;
    font-weight: 300; font-size: 72px; line-height: 1; letter-spacing: 0;
  }
  .b12 {
    position: absolute; left: 256px; top: 445px;
    font-weight: 700; font-size: 165px; line-height: 1; letter-spacing: 0;
  }
  .volume {
    position: absolute; left: 266px; top: 615px;
    font-size: 20px; font-weight: 700; color: var(--white);
  }
  .swoosh { position: absolute; left: 0; top: 0; width: 640px; height: 800px; }
  .format-band {
    position: absolute; left: 0; bottom: 0; width: 640px; height: 72px;
    display: flex; align-items: center; justify-content: center;
    color: var(--white); font-weight: 400; font-size: 40px; letter-spacing: 0.5px;
    text-transform: uppercase;
  }
</style>
</head>
<body>
  <main class="label">
    <div class="drop-visual" role="img" aria-label="Glossy blue liquid drop with small floating droplets"></div>

    <svg class="swoosh" viewBox="0 0 640 800" aria-hidden="true">
      <defs>
        <linearGradient id="silverLine" x1="0" y1="0" x2="1" y2="0">
          <stop offset="0" stop-color="var(--silver-dark)"/>
          <stop offset="0.5" stop-color="var(--silver-light)"/>
          <stop offset="1" stop-color="var(--silver-dark)"/>
        </linearGradient>
      </defs>
      <path d="M240,720 C430,690 560,620 640,515 L640,575 C520,670 400,705 240,722 Z" fill="var(--accent-blue)"/>
      <path d="M0,738 C230,718 470,690 640,585 L640,800 L0,800 Z" fill="var(--band-blue)"/>
      <path d="M0,724 C230,706 460,678 640,572" fill="none" stroke="url(#silverLine)" stroke-width="12"/>
      <rect x="0" y="728" width="640" height="72" fill="var(--band-blue)"/>
    </svg>

    <div class="brand-name">ZULMO</div>

    <h1 class="product-title">
      <span class="vitamin">VITAMIN</span>
      <span class="b12">B12</span>
    </h1>
    <p class="volume">2fl oz (60ml)</p>

    <p class="format-band">Liquid Dietary Supplement</p>
  </main>
</body>
</html>
```